Redesign Of Current Landing Page

I need to redesign this landing page https://www.brightoakpromos.biz/?page=landing&landing=23 (Please do not opt in because when you do it will show you the home page. Please clear your cookies before going to this url above to view the 1 page landing page.)

Please use my updated website as a reference for colors and logo.
http://layoutcraftzone.com/dh/bopg/index.html

I would like the call to action to be a button that opens into a lead form...

Button would be "Download Samples"

small business owners

Marketing

1 page

Designer to choose colors to be used in the design.

• must be full responsive on all devices
• must have a legitimate professional apeal to it
• open

```html
<!DOCTYPE html>
<html lang="en">
<head>
<meta charset="utf-8">
<title>Bright Oak Promos – Attract More Customers</title>
<link href="https://fonts.googleapis.com/css2?family=Roboto:wght@300;400;500;700&family=Lato:wght@400;700&display=swap" rel="stylesheet">
<style>
:root{
  --navy:#0e1722;
  --blue:#1a73c9;
  --hero-a:#3546c8;
  --hero-b:#2f6ae0;
  --orange:#ffa800;
  --orange-dark:#e08f00;
  --ink:#333a44;
  --muted:#777d85;
  --rule:#d8d8d8;
  --white:#ffffff;
  --dark:#141414;
}
*{box-sizing:border-box;margin:0;padding:0}
html,body{width:730px;height:1200px;overflow:hidden;background:var(--white);font-family:"Roboto",sans-serif;color:var(--ink)}
.page{width:730px;height:1200px;position:relative}
.btn{display:inline-block;background:var(--orange);color:var(--white);font-size:10px;font-weight:400;border-bottom:2px solid var(--orange-dark);text-decoration:none;text-align:center}
.accent{color:var(--blue)}
.section-title{font-size:15px;font-weight:700;text-transform:uppercase;text-align:center;letter-spacing:.1px}

/* header */
.site-header{height:42px;background:var(--navy);display:flex;align-items:center;justify-content:space-between;padding:0 142px}
.brand{display:flex;align-items:center;gap:6px;color:var(--blue);font-size:12px;font-weight:700;letter-spacing:.4px}
.brand-mark{width:11px;height:11px;background:var(--blue)}
.contacts{display:flex;align-items:center;gap:8px;font-size:7.5px;font-weight:500;color:var(--blue)}
.contacts .sep{width:1px;height:10px;background:#3a4350}

/* hero */
.hero{height:246px;position:relative;background:linear-gradient(90deg,var(--hero-a) 0%,var(--hero-b) 60%,#2a5fd3 100%);overflow:hidden}
.hero-collage{position:absolute;right:0;top:0;width:285px;height:246px;background:linear-gradient(135deg,#6d7fb8 0%,#c9894f 30%,#3f8fc4 55%,#d9b78a 80%,#1f4f8a 100%);-webkit-mask-image:linear-gradient(90deg,transparent 0,#000 70px);mask-image:linear-gradient(90deg,transparent 0,#000 70px)}
.hero-copy{position:absolute;left:142px;top:63px;color:var(--white)}
.hero-copy h1{font-size:20px;font-weight:500;margin-bottom:5px}
.hero-copy p{font-size:10px;font-weight:300;line-height:14.5px}
.hero-copy .btn{margin-top:11px;width:126px;height:25px;line-height:23px;font-size:8.5px}

/* incentives */
.incentives{height:239px;padding-top:25px;text-align:center}
.incentives .section-title{color:var(--ink);margin-bottom:15px}
.intro{font-size:5.6px;color:var(--muted);line-height:7.5px;width:400px;margin:0 auto 7px}
.icon-row{display:flex;justify-content:center;gap:35px;margin-top:16px}
.icon-item{width:40px;display:flex;flex-direction:column;align-items:center}
.icon-circle{width:40px;height:40px;border-radius:50%;background:var(--blue);border:2px solid #d9e6f3;display:flex;align-items:center;justify-content:center}
.icon-circle svg{width:20px;height:20px}
.icon-label{font-size:6.3px;margin-top:7px;width:80px;line-height:8px;color:var(--ink)}
.btn-outline{display:inline-block;margin-top:17px;width:106px;height:22px;line-height:20px;border:1.5px solid var(--blue);color:var(--blue);font-size:6.8px;font-weight:500;border-radius:2px}

/* why */
.why{height:241px;background:radial-gradient(ellipse at 50% 40%,#242424 0%,var(--dark) 70%);padding-top:21px;text-align:center;color:var(--white)}
.why .intro{color:#d8d8d8;width:450px}
.why .section-title{margin-bottom:14px}
.why .icon-circle{border-color:#2e3e55}
.why .icon-label{color:#e5e5e5}
.why .btn{margin-top:25px;width:127px;height:25px;line-height:23px;font-size:8.5px}

/* how */
.how{height:104px;padding-top:24px;text-align:center}
.how .section-title{margin-bottom:14px}

/* testimonials */
.testimonials{height:286px;text-align:center;padding-top:0}
.testimonials .section-title{margin-bottom:6px}
.title-rule{width:268px;height:1px;background:var(--rule);margin:0 auto;position:relative}
.title-rule::after{content:"";position:absolute;left:110px;top:-1px;width:48px;height:2px;background:var(--blue)}
.quote{position:relative;width:360px;margin:17px auto 0;font-family:"Lato",sans-serif;font-size:5.8px;line-height:9.6px;color:#222}
.quote-mark{position:absolute;top:-4px;width:20px;height:20px}
.quote-mark.open{left:-33px}
.quote-mark.close{right:-33px}
.author{margin-top:6px;font-size:8.5px;font-weight:700;color:var(--blue);letter-spacing:.3px}
.avatars{display:flex;justify-content:center;gap:6px;margin-top:28px;position:relative}
.avatar{width:44px;height:44px;border-radius:50%;background:radial-gradient(circle at 50% 40%,#8a8f96,#2c2f33)}
.avatar.active{border:2px solid var(--blue);background:radial-gradient(circle at 50% 40%,#dfe4ef,#7d93b3);position:relative}
.avatar.active::before{content:"";position:absolute;left:15px;top:-9px;border:6px solid transparent;border-bottom-color:var(--blue)}
.avatar.warm{background:radial-gradient(circle at 50% 40%,#e3c19a,#9b6e4a)}
.avatar.dark{background:radial-gradient(circle at 50% 40%,#6b5a55,#1e1a1a)}
.testimonials .btn{margin-top:21px;width:160px;height:22px;line-height:20px;font-size:7.5px;font-weight:500}

/* footer */
.site-footer{position:absolute;left:0;bottom:0;width:730px;height:42px;background:var(--navy);display:flex;align-items:center;justify-content:center;font-size:5.8px;color:var(--blue)}
</style>
</head>
<body>
<div class="page">

  <header class="site-header">
    <div class="brand"><span class="brand-mark"></span>BRIGHT OAK PROMOS</div>
    <div class="contacts">
      <svg width="8" height="8" viewBox="0 0 10 10"><circle cx="5" cy="5" r="5" fill="#1a73c9"/><path d="M3.2 2.6c.3-.3.6-.2.8.1l.4.7c.1.2 0 .4-.1.5l-.3.3c.3.6.8 1.1 1.4 1.4l.3-.3c.1-.1.3-.2.5-.1l.7.4c.3.2.4.5.1.8-.5.6-1 .6-1.7.3-1-.5-1.8-1.3-2.3-2.3-.3-.7-.3-1.2.2-1.8z" fill="#0e1722"/></svg>
      <span>USA Office : 619-555-0142</span>
      <span class="sep"></span>
      <span>International : 1-800-555-0199</span>
      <span class="sep"></span>
    </div>
  </header>

  <section class="hero">
    <div class="hero-collage" role="img" aria-label="Collage of travel rewards: airliner in flight, resort hotel with pool, spa massage, shopping cart and city skyline"></div>
    <div class="hero-copy">
      <h1>Attract More Customers</h1>
      <p>Who Spend More Money with your Business<br>More by providing them real incentives</p>
      <a class="btn" href="#">Download Samples</a>
    </div>
  </section>

  <section class="incentives">
    <h2 class="section-title">High Value Incentives <span class="accent">for Every Business</span></h2>
    <p class="intro">Imagine being able to create exciting give away promotions that will boost your sales without ever having to worry about cost.</p>
    <p class="intro">Bright Oak Promo Group, Inc. provides high-perceived value promotional incentives to businesses that want to advertise an exciting Give Away that will instantly attract more customers from your existing advertising efforts.</p>
    <p class="intro" style="margin-top:12px">Your business can give away incentive certificates that are redeemable for every kind of business including</p>
    <div class="icon-row">
      <div class="icon-item"><div class="icon-circle"><svg viewBox="0 0 20 20" fill="none" stroke="#fff" stroke-width="1.2"><rect x="3" y="5" width="14" height="11"/><path d="M6 8h2v2H6zM9 8h2v2H9zM12 8h2v2h-2zM6 12h2v2H6zM9 12h2v2H9zM12 12h2v2h-2zM5 3v2M15 3v2"/></svg></div><span class="icon-label">Luxury Hotel &amp; Resort Stays</span></div>
      <div class="icon-item"><div class="icon-circle"><svg viewBox="0 0 20 20" fill="#fff"><path d="M2 10.5c0-.6 1-.9 2-.9h4L5 4h2l5 5.6h4c1 0 2 .4 2 .9s-1 .9-2 .9h-4L7 17H5l3-5.6H4c-1 0-2-.3-2-.9z"/></svg></div><span class="icon-label">Air Line Tickets</span></div>
      <div class="icon-item"><div class="icon-circle"><svg viewBox="0 0 20 20" fill="none" stroke="#fff" stroke-width="1.2"><path d="M3 11h14l-2 5H5zM6 11V7h8v4M8 7V4h4v3M2 17c2 1 3-1 4 0s3 1 4 0 3 1 4 0 3 1 4 0"/></svg></div><span class="icon-label">Cruises</span></div>
      <div class="icon-item"><div class="icon-circle"><svg viewBox="0 0 20 20" fill="none" stroke="#fff" stroke-width="1.2"><rect x="4" y="3" width="8" height="14" rx="1"/><path d="M6 6h4v3H6zM12 8l3 2v5a1 1 0 0 0 2 0V8l-2-2"/></svg></div><span class="icon-label">Cash for Gas</span></div>
      <div class="icon-item"><div class="icon-circle"><svg viewBox="0 0 20 20" fill="#fff"><path d="M4 13a6 6 0 0 1 12 0zM2 14h16v1.5H2zM9 5.5h2v1.6H9z"/></svg></div><span class="icon-label">Dining</span></div>
      <div class="icon-item"><div class="icon-circle"><svg viewBox="0 0 20 20" fill="none" stroke="#fff" stroke-width="1.2"><rect x="4" y="5" width="12" height="8"/><path d="M2 15h16"/></svg></div><span class="icon-label">Electronics</span></div>
    </div>
    <a class="btn-outline" href="#">Many More</a>
  </section>

  <section class="why">
    <h2 class="section-title">Why Offer Incentives <span class="accent">to Customers?</span></h2>
    <p class="intro">Lorem ipsum dolor sit amet, consectetur adipisicing elit, sed do eiusmod tempor incididunt ut labore et dolore magna aliqua. Ut enim ad minim veniam, quis nostrud exercitation ullamco laboris nisi ut aliquip ex ea commodo consequat. Duis aute irure dolor in reprehenderit in voluptate velit esse cillum dolore eu fugiat nulla pariatur. Excepteur sint occaecat cupidatat non proident, sunt in culpa qui.</p>
    <div class="icon-row" style="margin-top:28px">
      <div class="icon-item"><div class="icon-circle"><svg viewBox="0 0 20 20" fill="#fff"><rect x="3" y="13" width="2.5" height="4"/><rect x="7" y="11" width="2.5" height="6"/><rect x="11" y="8" width="2.5" height="9"/><rect x="15" y="5" width="2.5" height="12"/><path d="M3 10l5-4 3 2 4-4" stroke="#fff" fill="none" stroke-width="1"/></svg></div><span class="icon-label">Increase Responses From Ads</span></div>
      <div class="icon-item"><div class="icon-circle"><svg viewBox="0 0 20 20"><circle cx="10" cy="10" r="5" fill="none" stroke="#fff" stroke-width="3.5" stroke-dasharray="2.2 1.7"/><circle cx="10" cy="10" r="4" fill="#fff"/><circle cx="10" cy="10" r="1.6" fill="#1a73c9"/></svg></div><span class="icon-label">#1 Sales Closing Tool</span></div>
      <div class="icon-item"><div class="icon-circle"><svg viewBox="0 0 20 20" fill="none" stroke="#fff" stroke-width="1.1"><circle cx="10" cy="10" r="7" stroke-dasharray="1.5 1"/><circle cx="10" cy="10" r="4.5"/><path d="M7 10h6"/></svg></div><span class="icon-label">Build Brand Awareness &amp; Trust</span></div>
      <div class="icon-item"><div class="icon-circle"><svg viewBox="0 0 20 20" fill="none" stroke="#fff" stroke-width="1.2"><path d="M6 3h8v4a4 4 0 0 1-8 0zM6 5H3c0 3 2 4 3 4M14 5h3c0 3-2 4-3 4M10 11v3M7 17h6v-2H7z"/></svg></div><span class="icon-label">Incure Sales Over your Competition</span></div>
      <div class="icon-item"><div class="icon-circle"><svg viewBox="0 0 20 20" fill="none" stroke="#fff" stroke-width="1.2"><circle cx="10" cy="10" r="7"/><path d="M6.5 9a3.5 3.5 0 0 1 6.3-1.5M13.5 11a3.5 3.5 0 0 1-6.3 1.5M12.8 5.5v2h-2M7.2 14.5v-2h2"/></svg></div><span class="icon-label">Boost Repeat and Referral Business</span></div>
      <div class="icon-item"><div class="icon-circle"><svg viewBox="0 0 20 20" fill="#fff"><path d="M8 3h4l-1 2.5h-2zM9 6h2c3 2 5 5 5 8a3 3 0 0 1-3 3H7a3 3 0 0 1-3-3c0-3 2-6 5-8z"/><text x="10" y="15" font-size="6" text-anchor="middle" fill="#1a73c9" font-family="Roboto,sans-serif" font-weight="700">$</text></svg></div><span class="icon-label">Improve Retention Rates</span></div>
    </div>
    <a class="btn" href="#">Download Samples</a>
  </section>

  <section class="how">
    <h2 class="section-title">How Can <span class="accent">We Do It</span></h2>
    <p class="intro" style="width:432px">We help fill empty rooms for thousands of hotels and resorts in hundreds of destinations around the world as well as the major cruise lines. Hotels and resorts are rarely full so when we place someone in their empty rooms, they end up making it up when travelers spend money on room service, spa services, eat at their in-house restaurants, casino and take advantage of other amenities that drive revenue.</p>
    <p class="intro" style="width:432px;margin-top:8px">We also help over 18,000 restaurants, electronic manufacturers, the major gas companies and top grocery chains in the U.S and Canada increase brand awareness as well as increase customer loyalty.</p>
  </section>

  <section class="testimonials">
    <h2 class="section-title">Client <span class="accent">Testimonials</span></h2>
    <div class="title-rule"></div>
    <div class="quote">
      <svg class="quote-mark open" viewBox="0 0 20 20" fill="#d2d2d2"><path d="M1 19V11C1 6 3 3 8 2v3c-2 1-3 2-3 5h3v9zM11 19V11c0-5 2-8 7-9v3c-2 1-3 2-3 5h3v9z"/></svg>
      <svg class="quote-mark close" viewBox="0 0 20 20" fill="#d2d2d2"><path d="M1 1v8c0 5 2 8 7 9v-3c-2-1-3-2-3-5h3V1zM11 1v8c0 5 2 8 7 9v-3c-2-1-3-2-3-5h3V1z"/></svg>
      I have been using BOPG for 6 months and have been so impressed with this company. I have used the incentives with my customers to encourage repeat business and referrals. It has always been a pleasure to work with my consultant, Carla. She calls me by name when we talk on the phone, and treats me like a professional and a friend. I have had several clients redeem their incentives, and all were incredibly pleased with them. Redemption is easy and fast. This strengthens my belief in BOPG, and assures that I will use their services for a long time! I would reccomend BOPG to all my business associates, and anyone who needs an incentive program to take their business to the next level.
    </div>
    <div class="author">DANA M.</div>
    <div class="avatars">
      <div class="avatar" role="img" aria-label="Client portrait"></div>
      <div class="avatar active" role="img" aria-label="Portrait of Dana M."></div>
      <div class="avatar dark" role="img" aria-label="Client portrait"></div>
      <div class="avatar dark" role="img" aria-label="Client portrait"></div>
      <div class="avatar warm" role="img" aria-label="Client portrait"></div>
    </div>
    <a class="btn" href="#">SIGN UP FOR A 30 DAY RISK FREE TRIAL</a>
  </section>

  <footer class="site-footer">Copyright 2017 Bright Oak Promo Group, Inc. All rights reserved.</footer>
</div>
</body>
</html>
```